Interior Design/Decor and Staging Website

Current website: www.marlowcrestinteriors.example but need something lighter and more appealing. Logo is also being changed. I would like a clean cut look, modern and professional. Would like a slideshow for portfolio pictures, social media icons and logos of where the work has been featured: VORNA, Nest Wares, Durrandel, Tobias Quill, Plaza Furnishings, etc.

Target Market(s)

interior design and interior decor clients, both local and international.

Industry/Entity Type

Home Improvement

Number of Pages Required

5+ page

Font styles to use
Sans Serif

Requirements
Nice to have
• Testimonial page and Dwellr reviews.

```html
<!DOCTYPE html>
<html lang="en">
<head>
<meta charset="utf-8">
<title>Marlow Crest Interiors</title>
<link href="https://fonts.googleapis.com/css2?family=Lato:wght@400;700;900&family=Questrial&family=Open+Sans:wght@600;700&display=swap" rel="stylesheet">
<style>
:root{
  --header:rgba(30,30,30,.88);
  --logo-bg:#0b0b0b;
  --gold:#d9c79a;
  --white:#ffffff;
  --ink:#111111;
  --grey-text:#555555;
  --muted:#777777;
  --button:#4a4a4a;
  --green:#6f9a2a;
  --crimson:#b32a4e;
  --teal:#0ba3a8;
  --footer:#6a6a6a;
  --footer-bottom:#1c1c1c;
  --box-line:#d6d6d6;
}
*{margin:0;padding:0;box-sizing:border-box}
html,body{width:1200px;height:2347px;overflow:hidden;background:var(--white)}
body{position:relative;font-family:'Lato',sans-serif;color:var(--ink)}
.abs{position:absolute}

/* hero */
.hero{left:0;top:0;width:1200px;height:810px;
  background:linear-gradient(90deg,#e9e7e4 0%,#d8d6d3 18%,#7a1f22 30%,#6b1a1d 62%,#5e1619 80%,#3a3434 100%)}
.hero-floor{left:0;top:560px;width:1200px;height:250px;background:linear-gradient(180deg,#bdbab6,#8d8a87)}
.site-header{left:0;top:0;width:1200px;height:131px;background:var(--header)}
.brand{left:108px;top:0;width:278px;height:131px;background:var(--logo-bg);display:flex;align-items:center;justify-content:center;gap:12px}
.brand-mark{width:14px;height:14px;background:var(--gold)}
.brand-name{font-family:'Questrial',sans-serif;color:var(--gold);font-size:27px;line-height:1.1;letter-spacing:1px;text-transform:uppercase}
.nav{left:576px;top:38px;height:53px;display:flex;align-items:center;font-size:16px;color:var(--white);text-transform:uppercase}
.nav a{color:inherit;text-decoration:none;display:flex;align-items:center;justify-content:center;height:53px}
.nav .active{width:131px;background:var(--white);color:var(--ink)}
.nav .item{padding:0 40px}
.nav .sep{width:1px;height:18px;background:var(--white)}

/* service tiles */
.tiles{left:47px;top:557px;width:1105px;height:507px;display:grid;grid-template-columns:repeat(3,1fr);grid-template-rows:repeat(2,1fr);gap:2px}
.tile{position:relative;display:flex;align-items:center;justify-content:center;font-family:'Open Sans',sans-serif;font-weight:700;color:var(--white);font-size:33px;text-transform:uppercase;letter-spacing:.5px}
.tile-green{background:var(--green)}
.tile-crimson{background:var(--crimson)}
.tile-teal{background:var(--teal)}
.photo-living{background:linear-gradient(160deg,#e6e1d8,#a88a66 60%,#6e5a44)}
.photo-lounge{background:linear-gradient(160deg,#f2f0ec,#6e5750 45%,#d9d6d2)}
.photo-view{background:linear-gradient(160deg,#cfe0e6,#8fa69a 45%,#c7b8a2)}
.toggle{position:absolute;width:38px;height:38px;border-radius:50%;background:var(--white);top:793px}

/* welcome */
.welcome-title{left:0;top:1116px;width:1200px;text-align:center;font-weight:700;font-size:34px;letter-spacing:.5px;text-transform:uppercase}
.welcome-title span{color:#555}
.welcome-text{left:120px;top:1180px;width:960px;text-align:center;font-size:12.5px;line-height:23px;color:var(--muted)}
.read-more{left:512px;top:1269px;width:176px;height:55px;background:var(--button);color:var(--white);font-size:15px;display:flex;align-items:center;justify-content:center;text-transform:uppercase}

/* banner */
.banner{left:0;top:1377px;width:1200px;height:425px;background:linear-gradient(90deg,#8a8a8a,#bdbdbd 45%,#a9a9a9 75%,#7c7c7c)}
.banner-line{left:0;width:1200px;text-align:center;font-family:'Questrial',sans-serif;font-size:56px;color:var(--white);line-height:1}
.banner-line b{color:var(--ink);font-weight:400}

/* partners */
.partners{left:66px;top:1851px;display:flex;gap:9px}
.partner{width:205px;height:103px;border:2px solid var(--box-line);display:flex;align-items:center;justify-content:center;font-size:22px;font-weight:700;color:#333}
.dots{left:0;top:1991px;width:1200px;display:flex;justify-content:center;gap:16px;align-items:center}
.dot{width:11px;height:11px;border-radius:50%;background:#555}
.dot.on{width:18px;height:18px;border:2px solid #555;background:var(--white);position:relative}
.dot.on::after{content:"";position:absolute;left:3px;top:3px;width:8px;height:8px;border-radius:50%;background:#222}

/* footer */
.footer{left:0;top:2053px;width:1200px;height:216px;background:var(--footer);color:var(--white)}
.f-head{top:40px;font-size:17px;font-weight:700;text-transform:uppercase}
.f-links{left:47px;top:70px;list-style:none;font-size:12px}
.f-links li{height:28.5px;display:flex;align-items:center;gap:14px}
.f-links li::before{content:"";border-left:5px solid var(--white);border-top:4px solid transparent;border-bottom:4px solid transparent}
.field{border:1px solid #bbb;width:156px;height:40px;font-size:12px;font-style:italic;color:#ddd;padding:0 12px;display:flex;align-items:center}
.submit{left:255px;top:159px;width:130px;height:38px;background:var(--footer-bottom);font-size:14px;display:flex;align-items:center;justify-content:center;text-transform:uppercase}
.f-info{left:654px;top:72px;font-size:12.5px;line-height:28px}
.social{left:940px;top:89px;display:flex;gap:12px}
.social span{width:34px;height:34px;border-radius:50%;background:var(--white)}
.legal{left:0;top:2269px;width:1200px;height:78px;background:var(--footer-bottom);color:var(--white);font-size:12px;padding-left:72px;display:flex;align-items:center}
</style>
</head>
<body>

<div class="abs hero" role="img" aria-label="Living room with red panelled wall, grey sofas with zebra cushions, framed prints and floating staircase"></div>
<div class="abs hero-floor" role="img" aria-label="Living room floor"></div>

<header class="abs site-header">
  <div class="abs brand"><span class="brand-mark"></span><span class="brand-name">Marlow Crest<br>Interiors</span></div>
  <nav class="abs nav">
    <a class="active" href="#">Home</a>
    <a class="item" href="#">Service</a><span class="sep"></span>
    <a class="item" href="#">Gallery</a><span class="sep"></span>
    <a class="item" href="#">Contacts</a>
  </nav>
</header>

<section class="abs tiles">
  <div class="tile tile-green">Interior Decor</div>
  <div class="tile photo-living" role="img" aria-label="Open plan living room with glass table and wooden shelving"></div>
  <div class="tile tile-crimson">Restyle &amp; Redesign</div>
  <div class="tile photo-lounge" role="img" aria-label="Lounge with brown feature wall, white sofa and framed art"></div>
  <div class="tile tile-teal">Home Staging</div>
  <div class="tile photo-view" role="img" aria-label="Bright living room with sofa and waterfront view"></div>
</section>
<svg class="abs toggle" style="left:204px" viewBox="0 0 38 38"><path d="M12 16l7 7 7-7" fill="none" stroke="#222" stroke-width="2.5"/></svg>
<svg class="abs toggle" style="left:580px" viewBox="0 0 38 38"><path d="M12 22l7-7 7 7" fill="none" stroke="#222" stroke-width="2.5"/></svg>
<svg class="abs toggle" style="left:955px" viewBox="0 0 38 38"><path d="M12 16l7 7 7-7" fill="none" stroke="#222" stroke-width="2.5"/></svg>

<h1 class="abs welcome-title">Welcome to <span>Marlow Crest Interiors</span></h1>
<p class="abs welcome-text">Lorem ipsum dolor sit amet, consectetur adipiscing elit, sed do eiusmod tempor incididunt ut labore et dolore magna aliqua. Ut enim ad minim veniam, quis nostrud exercitation ullamco laboris nisi ut aliquip ex ea commodo consequat. Duis aute irure dolor in reprehenderit in voluptate velit esse cillum dolore eu fugiat nulla pariatur. Excepteur sint occaecat cupidatat non proident, sunt in culpa qui officia deserunt mollit anim id est laborum.</p>
<div class="abs read-more">Read More</div>

<section class="abs banner" role="img" aria-label="Greyscale bathroom with freestanding tub, plants and sea view"></section>
<p class="abs banner-line" style="top:1530px"><b>H</b>ighest <b>Q</b>uality <b>M</b>aterials</p>
<p class="abs banner-line" style="top:1597px"><b>A</b>nd <b>P</b>erfect <b>E</b>xperience</p>

<section class="abs partners">
  <div class="partner">Tobias Quill</div>
  <div class="partner">VORNA</div>
  <div class="partner">Grand Hearth</div>
  <div class="partner">Nest Wares</div>
  <div class="partner">Durrandel</div>
</section>
<div class="abs dots"><span class="dot"></span><span class="dot on"></span><span class="dot"></span></div>

<footer class="abs footer">
  <h3 class="abs f-head" style="left:47px">About Us</h3>
  <ul class="abs f-links"><li>Home</li><li>About Us</li><li>Service</li><li>Gallery</li><li>Contact Us</li></ul>

  <h3 class="abs f-head" style="left:250px">Contact Us</h3>
  <div class="abs field" style="left:255px;top:69px">Name</div>
  <div class="abs field" style="left:415px;top:69px">Phone</div>
  <div class="abs field" style="left:255px;top:114px">E-mail</div>
  <div class="abs field" style="left:415px;top:114px">Message</div>
  <div class="abs submit">Submit</div>

  <h3 class="abs f-head" style="left:651px">Have Questions?</h3>
  <div class="abs f-info">555-014-2290<br>info@marlowcrest.example<br>Lorem Ipsum is simply dummy</div>

  <h3 class="abs f-head" style="left:943px">Follow Us</h3>
  <div class="abs social" aria-label="Social media links"><span></span><span></span><span></span><span></span></div>
</footer>
<div class="abs legal">Copy Right @ 2016 Marlow Crest. All Rights Reserved</div>

</body>
</html>
```